Improved Business Card, Government Contracting

We are looking to update the design of our business cards. We would like to create a template that can be used for future employees and easy to update.

Halvorsen Advisory Partners, LLC is a Service Disabled Veteran Owned Small Business with headquarters located in Tallow Creek, NV. Our current website is www.hapteam.com. We have contracts in KS and VA with expansion opportunities in various other states. Our primary line of work is within government contracting and providing consulting services to various organizations within the Bureau of Frontier Works. We would like to project a professional image of our company that is consistent with the industry. Provided are previous versions of our business card template that shows our logo as well. We would like to make sure the information on the cards are easily noticeable .

Target Market(s)

Government Officials
Fellow Small Business Contractors
Large Business Contractors (ex. TRUX, Keswell Barnaby, Pryde Okonjo Whitcombe)

Industry/Entity Type

Business

Contact Information for Business Card

Dale Fenwick
Office Manager
Halvorsen Advisory Partners
Ph: 555.555.0172
Email: d.fenwick@hapteam.us
www.hapteam.com

Requirements
Must have
• The business mailing address is:
• 31842 204th Lane
• Tallow Creek, NV 66099
Nice to have
• Embossed lettering

```html
<!DOCTYPE html>
<html lang="en">
<head>
<meta charset="utf-8">
<title>Halvorsen Advisory Partners – Business Card</title>
<link rel="stylesheet" href="https://fonts.googleapis.com/css2?family=Open+Sans:wght@600&family=Arimo:wght@400;700&display=swap">
<style>
  :root {
    --backdrop: #2a2a2c;
    --card-white: #ffffff;
    --brand-blue: #3a56a8;
    --accent-yellow: #f6ee5a;
    --wordmark: #ffffff;
    --emboss-ink: #c9d1e6;
    --emboss-ink-light: #6a6a6a;
  }
  html, body {
    margin: 0;
    width: 1200px;
    height: 900px;
    overflow: hidden;
    background: var(--backdrop);
  }
  .card-sheet {
    position: relative;
    width: 1200px;
    height: 900px;
  }
  .card {
    position: absolute;
    left: 320px;
    width: 560px;
    height: 320px;
    box-shadow: 0 12px 30px rgba(0, 0, 0, 0.6);
  }
  .card--front { top: 90px; }
  .card--back { top: 480px; }
  .card svg { display: block; }
  .card-bg { fill: var(--card-white); }
  .panel { fill: var(--brand-blue); }
  .rule {
    fill: none;
    stroke: var(--accent-yellow);
    stroke-width: 6;
  }
  .wordmark {
    font-family: "Open Sans", sans-serif;
    font-weight: 600;
    fill: var(--wordmark);
  }
  .holder-name, .holder-title {
    font-family: "Arimo", sans-serif;
    font-weight: 700;
    fill: var(--emboss-ink-light);
    filter: url(#emboss);
  }
  .contact-line {
    font-family: "Arimo", sans-serif;
    font-size: 15px;
    fill: var(--emboss-ink);
    filter: url(#emboss);
  }
</style>
</head>
<body>
<main class="card-sheet">

  <svg width="0" height="0" aria-hidden="true" style="position:absolute">
    <defs>
      <filter id="emboss" x="-5%" y="-30%" width="110%" height="160%">
        <feDropShadow dx="0.8" dy="1" stdDeviation="0.4" flood-color="#000" flood-opacity="0.5"/>
      </filter>
    </defs>
  </svg>

  <section class="card card--front" aria-label="Card front">
    <svg width="560" height="320" viewBox="0 0 560 320">
      <rect class="card-bg" width="560" height="320"/>
      <rect class="panel" x="0" y="0" width="560" height="230"/>
      <line class="rule" x1="0" y1="233" x2="560" y2="233"/>
      <text class="wordmark" x="280" y="128" font-size="30" text-anchor="middle">Halvorsen Advisory Partners</text>
    </svg>
  </section>

  <section class="card card--back" aria-label="Card back">
    <svg width="560" height="320" viewBox="0 0 560 320">
      <rect class="card-bg" width="560" height="320"/>
      <rect class="panel" x="0" y="0" width="560" height="86"/>
      <rect class="panel" x="290" y="86" width="270" height="234"/>
      <line class="rule" x1="0" y1="89" x2="290" y2="89"/>
      <line class="rule" x1="287" y1="89" x2="287" y2="320"/>
      <text class="wordmark" x="32" y="52" font-size="22">Halvorsen Advisory Partners</text>

      <text class="holder-name" x="36" y="200" font-size="20">Dale Fenwick</text>
      <text class="holder-title" x="36" y="222" font-size="15">Office Manager</text>

      <text class="contact-line" x="318" y="150">Ph: 555.555.0172</text>
      <text class="contact-line" x="318" y="190">31842 204th Lane</text>
      <text class="contact-line" x="318" y="210">Tallow Creek, NV 66099</text>
      <text class="contact-line" x="318" y="240">d.fenwick@hapteam.us</text>
      <text class="contact-line" x="318" y="260">www.hapteam.com</text>
    </svg>
  </section>

</main>
</body>
</html>
```